One-Page Redesign (Member's Area of Conference-Call Service)

Please take my mockup (THE ATTACHED PNG FILE) and make it look like a modern, cool, professional SaaS. Only restriction is you have to use free web fonts. And the fonts shouldn't have weird things like some letters or numbers being odd-sized.

If we work well together, I have an infinite amount of design projects for you to do.

Target Market(s)

Small Business Owners

Industry/Entity Type

Call

Number of Pages Required

1 page

Font styles to use
Sans Serif

Colors

Designer to choose colors to be used in the design.

Requirements
Must have
• It must look like a single, cohesive design -- with the menu and the content working together. It must be readable. It must be organized. It must give people an awesome first impression
Nice to have
• I'd like it to feel welcoming, not cold
Should not have
• It should not look like a damn template... It should not look amateurish

```html
<!DOCTYPE html>
<html lang="en">
<head>
<meta charset="utf-8">
<title>Linkwell – Member's Area</title>
<link href="https://fonts.googleapis.com/css2?family=Open+Sans:wght@400;600;700&family=Oswald:wght@500&display=swap" rel="stylesheet">
<style>
:root{
  --navy:#0b2540;
  --blue:#16507f;
  --teal:#1f7fa3;
  --green:#3cb43c;
  --green-soft:#e6f5e3;
  --ink:#2b2b2b;
  --grey:#8a8f94;
  --line:#dcdcdc;
  --board:#ffffff;
}
*{box-sizing:border-box;margin:0;padding:0}
html,body{width:1200px;height:2588px;overflow:hidden;background:var(--board);font-family:"Open Sans",Arial,sans-serif;color:var(--ink)}
.board{position:relative;width:1200px;height:2588px}
.board-label{position:absolute;top:128px;font-family:"Oswald","Arial Narrow",sans-serif;font-weight:500;font-size:46px;letter-spacing:1px;color:#3a3a3a}
.board-label--desktop{left:100px}
.board-label--mobile{left:872px}
.frame{position:absolute;background:#fff;box-shadow:0 0 0 1px var(--line);overflow:hidden}
.desktop{left:120px;top:220px;width:620px;height:2272px}
.mobile{left:860px;top:220px;width:220px;height:1280px}
.abs{position:absolute}
.hero{left:0;top:0;width:100%;height:300px;clip-path:polygon(0 0,100% 0,100% 82%,50% 100%,0 82%)}
.hero-art{position:absolute;inset:0;background:radial-gradient(ellipse at 75% 60%,rgba(42,138,176,.75),transparent 60%),radial-gradient(ellipse at 20% 20%,rgba(26,91,138,.8),transparent 55%),linear-gradient(135deg,var(--navy) 0%,var(--blue) 50%,var(--navy) 100%)}
.nav{position:absolute;left:30px;right:30px;top:18px;display:flex;align-items:center;justify-content:space-between;color:#fff;font-size:11px}
.brand{font-weight:700;font-size:13px;color:#fff}
.nav-links{display:flex;gap:18px}
.btn{display:inline-block;background:var(--green);color:#fff;font-weight:600;border-radius:2px;text-align:center}
.btn--sm{font-size:9px;padding:4px 12px}
.hero-title{left:0;right:0;top:84px;text-align:center;color:#fff;font-size:26px;font-weight:600}
.hero-text{left:160px;right:160px;top:122px;text-align:center;color:#dbe7f0;font-size:10px;line-height:1.6}
.hero-cta{position:absolute;left:270px;top:192px;width:80px;font-size:10px;padding:6px 0}
.spine{left:309px;width:2px;background:var(--green-soft)}
.section-title{text-align:center;font-size:24px;font-weight:600;line-height:1.25;color:var(--ink)}
.body-text{font-size:10px;line-height:1.6;color:var(--grey)}
.photo--office{background:linear-gradient(120deg,#6d4f3a,#b8916c 55%,#3e3a38)}
.photo--meeting{background:linear-gradient(120deg,#3b4650,#8b939a 50%,#c7b59c)}
.photo--desk{background:linear-gradient(180deg,rgba(20,40,50,.35),rgba(20,40,50,.55)),linear-gradient(110deg,#6c7d6e,#a59a7f 50%,#4d5b58)}
.rule{height:2px;background:var(--green)}
.cta-circle{left:260px;top:1100px;width:100px;height:100px;border-radius:50%;background:var(--green);color:#fff;font-size:10px;font-weight:700;display:flex;align-items:center;justify-content:center;text-align:center;line-height:1.3;box-shadow:0 0 0 8px var(--green-soft)}
.band-title{left:0;right:0;top:1320px;text-align:center;color:#fff;font-size:22px;font-weight:600}
.band-title span,.accent{color:var(--green)}
.card{background:#fff;box-shadow:0 2px 8px rgba(0,0,0,.12);padding:16px;text-align:center}
.card-media{height:70px;border:1px solid var(--line);display:flex;align-items:center;justify-content:center;font-size:10px;color:var(--grey);margin-bottom:12px}
.stars{color:var(--green);font-size:16px;letter-spacing:3px}
.social-item{display:flex;gap:10px;align-items:flex-start;margin-bottom:14px}
.social-mark{flex:0 0 26px;height:26px;background:#e9ecef;border:1px solid var(--line)}
.footer{left:0;bottom:0;width:100%;height:122px;background:linear-gradient(135deg,var(--navy),var(--blue));color:#cfdbe6;padding:16px 30px;display:flex;gap:40px;font-size:8px;line-height:1.6}
.footer h4{color:#fff;font-size:13px;margin-bottom:6px}
.footer h4 span{color:var(--green)}
.dots{display:flex;gap:6px}
.dots i{width:16px;height:16px;border-radius:50%;border:1px solid #cfdbe6;display:block}
.m .body-text{font-size:6px}
</style>
</head>
<body>
<div class="board">
  <div class="board-label board-label--desktop">DESKTOP</div>
  <div class="board-label board-label--mobile">MOBILE</div>

  <!-- Desktop page -->
  <div class="frame desktop">
    <div class="abs spine" style="top:290px;height:820px"></div>
    <header class="abs hero">
      <div class="hero-art" role="img" aria-label="Blue faceted abstract background"></div>
      <nav class="nav">
        <span class="brand">Linkwell</span>
        <span class="nav-links"><span>Home</span><span>Services</span><span>Contact</span></span>
        <span class="btn btn--sm">Log In</span>
      </nav>
      <h1 class="abs hero-title">About</h1>
      <p class="abs hero-text">Lorem ipsum dolor sit amet, consectetur adipiscing elit, sed do eiusmod tempor incididunt ut labore et dolore magna aliqua. Ut enim ad minim veniam, quis nostrud.</p>
      <span class="btn hero-cta">Learn More</span>
    </header>

    <section>
      <h2 class="abs section-title" style="left:0;right:0;top:340px">Lorem ipsum<br>dolor sit amet.</h2>
      <p class="abs body-text" style="left:200px;right:200px;top:410px;text-align:center">Lorem ipsum dolor sit amet, consectetur adipiscing elit, sed do eiusmod tempor incididunt ut labore et dolore.</p>
    </section>

    <section>
      <div class="abs photo--office" style="left:0;top:500px;width:230px;height:220px" role="img" aria-label="Businessman in a suit working at a laptop in an office"></div>
      <p class="abs body-text" style="left:330px;right:40px;top:560px">Lorem ipsum dolor sit amet, consectetur adipiscing elit, sed do eiusmod tempor incididunt ut labore et dolore magna aliqua. Ut enim ad minim veniam.</p>
      <span class="abs btn btn--sm" style="left:380px;top:650px">Learn More</span>
      <div class="abs rule" style="left:460px;right:0;top:660px"></div>
    </section>

    <section>
      <div class="abs photo--meeting" style="left:300px;top:790px;width:320px;height:230px" role="img" aria-label="Two colleagues in a meeting at a table with a laptop"></div>
      <p class="abs body-text" style="left:40px;width:220px;top:860px">Lorem ipsum dolor sit amet, consectetur adipiscing elit, sed do eiusmod tempor incididunt ut labore et dolore magna aliqua. Ut enim ad minim veniam.</p>
      <span class="abs btn btn--sm" style="left:170px;top:950px">Learn More</span>
      <div class="abs rule" style="left:0;width:170px;top:960px"></div>
    </section>

    <div class="abs cta-circle">START THE<br>PROCESS</div>

    <section>
      <div class="abs photo--desk" style="left:0;top:1250px;width:620px;height:240px;clip-path:polygon(0 12%,100% 0,100% 100%,0 100%)" role="img" aria-label="Desk with a vintage typewriter and notebook"></div>
      <h2 class="abs band-title">Our Helpful <span>Experts</span></h2>
      <div class="abs" style="left:30px;right:30px;top:1370px;display:grid;grid-template-columns:repeat(3,1fr);gap:14px">
        <div class="card"><div class="card-media">Your Image Here</div><p class="body-text">Lorem ipsum dolor sit amet, consectetur adipiscing elit sed do eiusmod.</p></div>
        <div class="card"><div class="card-media">Your Image Here</div><p class="body-text">Lorem ipsum dolor sit amet, consectetur adipiscing elit sed do eiusmod.</p></div>
        <div class="card"><div class="card-media">Your Image Here</div><p class="body-text">Lorem ipsum dolor sit amet, consectetur adipiscing elit sed do eiusmod.</p></div>
        <div class="card"><div class="card-media">Your Image Here</div><p class="body-text">Lorem ipsum dolor sit amet, consectetur adipiscing elit sed do eiusmod.</p></div>
        <div class="card"><div class="card-media">Your Image Here</div><p class="body-text">Lorem ipsum dolor sit amet, consectetur adipiscing elit sed do eiusmod.</p></div>
        <div class="card"><div class="card-media">Your Image Here</div><p class="body-text">Lorem ipsum dolor sit amet, consectetur adipiscing elit sed do eiusmod.</p></div>
      </div>
    </section>

    <section>
      <h2 class="abs" style="left:0;right:0;top:1775px;text-align:center;font-size:20px;font-weight:600">Connect With <span class="accent">Helpful Experts</span> Today</h2>
      <span class="abs btn" style="left:240px;top:1815px;width:140px;padding:7px 0;font-size:12px">(123) 456-7890</span>
    </section>

    <section>
      <h3 class="abs" style="left:60px;top:1880px;font-size:13px;font-weight:600">What Users are <span class="accent">Saying</span></h3>
      <div class="abs stars" style="left:80px;top:1900px">★★★★★</div>
      <div class="abs accent" style="left:30px;top:1920px;font-size:40px;font-weight:700;line-height:1">“</div>
      <p class="abs body-text" style="left:60px;width:230px;top:1930px">Lorem ipsum dolor sit amet, consectetur adipiscing elit, sed do eiusmod tempor incididunt ut labore et dolore magna aliqua.</p>
      <p class="abs body-text" style="left:60px;width:230px;top:1990px;text-align:center">– Jane Doe, Owner</p>
      <div class="abs rule" style="left:0;width:30px;top:1960px"></div>

      <h3 class="abs" style="left:330px;top:1880px;font-size:13px;font-weight:600">Social Media <span class="accent">Feed</span></h3>
      <div class="abs" style="left:330px;width:240px;top:1915px">
        <div class="social-item"><span class="social-mark"></span><p class="body-text">Lorem ipsum dolor sit amet, consectetur adipiscing elit sed do.</p></div>
        <div class="social-item"><span class="social-mark"></span><p class="body-text">Lorem ipsum dolor sit amet, consectetur adipiscing elit sed do.</p></div>
      </div>
      <div class="abs rule" style="left:590px;right:0;top:1960px"></div>
    </section>

    <footer class="abs footer">
      <div style="width:170px"><h4>About <span>Us</span></h4><p>Lorem ipsum dolor sit amet, consectetur adipiscing elit, sed do eiusmod tempor incididunt ut labore.</p></div>
      <div style="width:150px"><h4>Quick <span>Links</span></h4><p>Home<br>Services<br>Contact</p></div>
      <div><h4>Social <span>Media</span></h4><div class="dots"><i></i><i></i><i></i><i></i><i></i></div></div>
      <p class="abs" style="left:0;right:0;bottom:6px;text-align:center;font-size:7px">© Linkwell. All rights reserved.</p>
    </footer>
  </div>

  <!-- Mobile page -->
  <div class="frame mobile m">
    <header class="abs hero" style="height:160px">
      <div class="hero-art" role="img" aria-label="Blue faceted abstract background"></div>
      <nav class="nav" style="left:10px;right:10px;top:8px;font-size:6px"><span class="brand" style="font-size:7px">Linkwell</span><span class="btn" style="font-size:5px;padding:2px 6px">Log In</span></nav>
      <h1 class="abs hero-title" style="top:40px;font-size:14px">About</h1>
      <p class="abs hero-text" style="left:30px;right:30px;top:62px;font-size:5px">Lorem ipsum dolor sit amet, consectetur adipiscing elit, sed do eiusmod tempor.</p>
      <span class="abs btn" style="left:85px;top:100px;width:50px;font-size:5px;padding:3px 0">Learn More</span>
    </header>
    <p class="abs section-title" style="left:0;right:0;top:168px;font-size:9px">Lorem ipsum dolor sit amet.</p>
    <div class="abs photo--office" style="left:0;top:190px;width:220px;height:80px" role="img" aria-label="Businessman working at a laptop"></div>
    <p class="abs body-text" style="left:20px;right:20px;top:276px;text-align:center">Lorem ipsum dolor sit amet, consectetur adipiscing elit sed do.</p>
    <div class="abs photo--meeting" style="left:0;top:300px;width:220px;height:80px" role="img" aria-label="Two colleagues meeting at a table"></div>
    <p class="abs body-text" style="left:20px;right:20px;top:386px;text-align:center">Lorem ipsum dolor sit amet, consectetur adipiscing elit sed do.</p>
    <div class="abs cta-circle" style="left:95px;top:420px;width:30px;height:30px;font-size:4px;box-shadow:0 0 0 4px var(--green-soft)">START</div>
    <div class="abs" style="left:0;right:0;top:470px;height:340px;background:var(--green-soft)"></div>
    <div class="abs card" style="left:20px;right:20px;top:485px;height:130px;padding:8px"><div class="card-media" style="height:50px;font-size:6px">Your Image Here</div><p class="body-text">Lorem ipsum dolor sit amet, consectetur adipiscing elit sed do eiusmod.</p></div>
    <div class="abs card" style="left:20px;right:20px;top:630px;height:130px;padding:8px"><div class="card-media" style="height:50px;font-size:6px">Your Image Here</div><p class="body-text">Lorem ipsum dolor sit amet, consectetur adipiscing elit sed do eiusmod.</p></div>
    <p class="abs" style="left:0;right:0;top:776px;text-align:center;font-size:8px;font-weight:600">Connect With <span class="accent">Helpful Experts</span> Today</p>
    <span class="abs btn" style="left:75px;top:792px;width:70px;font-size:6px;padding:3px 0">(123) 456-7890</span>
    <p class="abs" style="left:10px;top:840px;font-size:9px;font-weight:600">Social Media <span class="accent">Feed</span></p>
    <div class="abs" style="left:10px;right:10px;top:860px;font-size:6px">
      <div class="social-item"><span class="social-mark" style="flex-basis:22px;height:22px"></span><p class="body-text">Lorem ipsum dolor sit amet, consectetur adipiscing elit.</p></div>
      <div class="social-item"><span class="social-mark" style="flex-basis:22px;height:22px"></span><p class="body-text">Lorem ipsum dolor sit amet, consectetur adipiscing elit.</p></div>
      <div class="social-item"><span class="social-mark" style="flex-basis:22px;height:22px"></span><p class="body-text">Lorem ipsum dolor sit amet, consectetur adipiscing elit.</p></div>
    </div>
    <div class="abs" style="left:0;right:0;top:1070px;height:160px;background:var(--green-soft)"></div>
    <p class="abs" style="left:0;right:0;top:1085px;text-align:center;font-size:8px;font-weight:600">What Users are <span class="accent">Saying</span></p>
    <div class="abs stars" style="left:0;right:0;top:1100px;text-align:center;font-size:10px">★★★★★</div>
    <p class="abs body-text" style="left:20px;right:20px;top:1122px;text-align:center">Lorem ipsum dolor sit amet, consectetur adipiscing elit, sed do eiusmod tempor incididunt ut labore.</p>
    <p class="abs body-text" style="left:20px;right:20px;top:1170px;text-align:center">– Jane Doe, Owner</p>
    <footer class="abs footer" style="height:50px;padding:8px;gap:10px;font-size:5px">
      <div><h4 style="font-size:7px">About</h4><p>Lorem ipsum dolor.</p></div>
      <div><h4 style="font-size:7px">Links</h4><p>Home</p></div>
      <div><h4 style="font-size:7px">Social</h4><div class="dots"><i style="width:6px;height:6px"></i><i style="width:6px;height:6px"></i><i style="width:6px;height:6px"></i></div></div>
    </footer>
  </div>
</div>
</body>
</html>
```